Label for Whiskey and Rum Bottle

We are a distillery. Whiskey and Rum We like to have a new label for our bottles. The whiskey bottles are in a wooden case. http://www.kornfaesser.ch/store/product/talwinkel-obermatt-single-malt-whiskey-nr-6 The Rum Bottles have no package. The label is even more important. http://www.kornfaesser.ch/store/product/talwinkel-obermatter-rum You can see the form of the bottles here www.kornfaesser.ch/store Whiskey and rum bottles are for a liter (50 cl) The labels can be with a picture or without. We would like to have something completely new. Therefore we don`t like to make much prescriptions concerning the design. We don`t like to give too much information (text) on the label. Just the information required by law. Consumers should understand the labels without long-reading. (The label-text is below) The 2 labels (Whiskey and rum) should look similar. Probably they have a different color or a different picture or .... It should be clear that the 2 products are from the same distillery. We have the intention to change all our existing labels over time. This gives designers the chance for follow-up projects.

Target Market(s)

Adults, liquor lovers

Requirements
Must have
• Information on the label is in German. (See "") Whiskey: - the name of the whiskey is "Talwinkel Obermatt Single Malt Whiskey" - The Whiskey was matured 5 years in a sherry "5 years in the sherry barrel stored" - The Alcohol content is 40% volumes "40% Vol "- The bottle contents 50 cl" 5 dl "- The distillery is" Distillery Brunnacher, Tornwil, www.kornfaesser.ch "- The producer is" Kelvor GmbH "Rum: - The name is" Talwinkel Obermatter Rum "- The alcohol content is 37% Volumes "37% Vol" - The bottle contens 50 cl "5 dl" - The distillery is "Distillery Brunnacher, Tornwil, www.kornfaesser.ch" - The producer is "Kelvor GmbH"
Nice to have
• Premium looking label Only front label preferred Only necessary text on the label
Should not have
• No special print techniques necessary No special paper form

```html
<!DOCTYPE html>
<html lang="de">
<head>
<meta charset="utf-8">
<title>Talwinkel Obermatter Rum – Etikett</title>
<link rel="stylesheet" href="https://fonts.googleapis.com/css2?family=Cinzel:wght@400;600&display=swap">
<style>
  :root {
    --page: #13202f;
    --label-ground: #3a261b;
    --parchment-light: #f2ecdf;
    --parchment-dark: #d8cbb1;
    --copper-light: #d9a27a;
    --copper: #9a4a2a;
    --copper-dark: #5e2716;
    --ink: #2c2a29;
    --url: #f3ede2;
  }
  html, body {
    margin: 0;
    width: 1200px;
    height: 1200px;
    overflow: hidden;
    background: var(--page);
  }
  .sheet {
    width: 1200px;
    height: 1200px;
    display: flex;
    flex-direction: column;
    align-items: center;
    justify-content: center;
    gap: 40px;
  }
  .label {
    width: 520px;
    height: 440px;
    display: block;
    font-family: "Cinzel", serif;
  }
  .label-ground { fill: var(--label-ground); }
  .oval-parchment { fill: url(#parchment); }
  .oval-rim { fill: none; stroke: url(#copper-rim); stroke-width: 7; }
  .oval-rim-inner { fill: none; stroke: var(--copper-dark); stroke-width: 1.2; opacity: .7; }
  .arc-title { font-size: 31px; fill: var(--ink); letter-spacing: 1px; }
  .arc-title .cap { font-size: 39px; }
  .product { font-size: 66px; fill: url(#copper-type); }
  .producer { font-size: 22px; fill: var(--ink); letter-spacing: 7px; }
  .producer-rule { stroke: var(--ink); stroke-width: 1; }
  .facts { font-size: 19px; fill: var(--ink); }
  .distillery-mark { fill: var(--copper); }
  .distillery { font-size: 15px; fill: var(--ink); }
  .web { font-size: 14px; fill: var(--url); letter-spacing: 3px; font-weight: 600; }
</style>
</head>
<body>
<svg width="0" height="0" style="position:absolute" aria-hidden="true">
  <defs>
    <radialGradient id="parchment" cx="50%" cy="45%" r="60%">
      <stop offset="0" stop-color="var(--parchment-light)"/>
      <stop offset="0.7" stop-color="#e8dfcc"/>
      <stop offset="1" stop-color="var(--parchment-dark)"/>
    </radialGradient>
    <linearGradient id="copper-rim" x1="0" y1="0" x2="1" y2="1">
      <stop offset="0" stop-color="var(--copper-dark)"/>
      <stop offset="0.35" stop-color="var(--copper-light)"/>
      <stop offset="0.65" stop-color="var(--copper)"/>
      <stop offset="1" stop-color="#f0d2b8"/>
    </linearGradient>
    <linearGradient id="copper-type" x1="0" y1="0" x2="0" y2="1">
      <stop offset="0" stop-color="var(--copper-dark)"/>
      <stop offset="0.55" stop-color="var(--copper)"/>
      <stop offset="1" stop-color="var(--copper-light)"/>
    </linearGradient>
    <path id="title-arc" d="M 72,238 A 192 162 0 0 1 448,238"/>
  </defs>
</svg>

<main class="sheet">
  <svg class="label label--rounded" viewBox="0 0 520 440" role="img" aria-label="Etikett Talwinkel Obermatter Rum, abgerundet">
    <rect class="label-ground" x="0" y="0" width="520" height="440" rx="48"/>
    <ellipse class="oval-parchment" cx="260" cy="200" rx="246" ry="182"/>
    <ellipse class="oval-rim" cx="260" cy="200" rx="246" ry="182"/>
    <ellipse class="oval-rim-inner" cx="260" cy="200" rx="238" ry="174"/>
    <text class="arc-title"><textPath href="#title-arc" startOffset="50%" text-anchor="middle"><tspan class="cap">T</tspan>ALWINKEL <tspan class="cap">O</tspan>BERMATTER</textPath></text>
    <text class="product" x="260" y="180" text-anchor="middle">RUM</text>
    <line class="producer-rule" x1="128" y1="198" x2="392" y2="198"/>
    <text class="producer" x="263" y="227" text-anchor="middle">KELVOR GMBH</text>
    <line class="producer-rule" x1="128" y1="236" x2="392" y2="236"/>
    <circle class="distillery-mark" cx="260" cy="283" r="17"/>
    <text class="facts" x="110" y="295">50 cl</text>
    <text class="facts" x="408" y="295" text-anchor="end">Al 37%</text>
    <text class="distillery" x="260" y="330" text-anchor="middle">BRENNEREI</text>
    <text class="distillery" x="260" y="348" text-anchor="middle">BRUNNACHER</text>
    <text class="web" x="260" y="414" text-anchor="middle">WWW.KORNFAESSER.CH</text>
  </svg>

  <svg class="label label--square" viewBox="0 0 520 440" role="img" aria-label="Etikett Talwinkel Obermatter Rum, rechteckig">
    <rect class="label-ground" x="0" y="0" width="520" height="440"/>
    <ellipse class="oval-parchment" cx="260" cy="200" rx="246" ry="182"/>
    <ellipse class="oval-rim" cx="260" cy="200" rx="246" ry="182"/>
    <ellipse class="oval-rim-inner" cx="260" cy="200" rx="238" ry="174"/>
    <text class="arc-title"><textPath href="#title-arc" startOffset="50%" text-anchor="middle"><tspan class="cap">T</tspan>ALWINKEL <tspan class="cap">O</tspan>BERMATTER</textPath></text>
    <text class="product" x="260" y="180" text-anchor="middle">RUM</text>
    <line class="producer-rule" x1="128" y1="198" x2="392" y2="198"/>
    <text class="producer" x="263" y="227" text-anchor="middle">KELVOR GMBH</text>
    <line class="producer-rule" x1="128" y1="236" x2="392" y2="236"/>
    <circle class="distillery-mark" cx="260" cy="283" r="17"/>
    <text class="facts" x="110" y="295">50 cl</text>
    <text class="facts" x="408" y="295" text-anchor="end">Al 37%</text>
    <text class="distillery" x="260" y="330" text-anchor="middle">BRENNEREI</text>
    <text class="distillery" x="260" y="348" text-anchor="middle">BRUNNACHER</text>
    <text class="web" x="260" y="414" text-anchor="middle">WWW.KORNFAESSER.CH</text>
  </svg>
</main>
</body>
</html>
```